Property letting UK website

I need a web design for a new Property letting company in the UK. I already have a logo that was produced and won by a pixel harbor logo designer last week.

I like modern designs and require ease of functionality and usage. I already have a domain name registered so need to be able to link to that domain.

Regards,

Miles.

Target Market(s)

UK property

Industry/Entity Type

It Company

Number of Pages Required

5+ page

Requirements
Must have
• Home page, Current properties to let page, About us page, Contact us page, Testimonials page and ability to link to chirpnet and Friendlane account.

```html
<!DOCTYPE html>
<html lang="en">
<head>
<meta charset="utf-8">
<title>Dwell-On — Property Letting</title>
<link href="https://fonts.googleapis.com/css2?family=Lato:ital,wght@0,400;0,700;1,400&family=Marcellus&family=PT+Serif:ital@0;1&display=swap" rel="stylesheet">
<style>
:root{
  --black:#000;
  --sky:#27a9e1;
  --sky-dark:#0d86c7;
  --navy:#0a3f78;
  --navy-2:#0b62aa;
  --orange:#f7941d;
  --paper:#f4f4f4;
  --ink:#555;
  --footer:#2a2a2a;
  --footer-text:#d8d8d8;
  --white:#fff;
}
*{margin:0;padding:0;box-sizing:border-box}
html,body{width:833px;height:1200px;overflow:hidden}
body{position:relative;background:var(--paper);font-family:"Lato",Arial,sans-serif;color:var(--ink)}
.abs{position:absolute}

/* header */
.topbar{left:0;top:0;width:833px;height:73px;background:linear-gradient(#111,#000)}
.brand{left:110px;top:16px;font-size:38px;color:var(--white);font-weight:400;letter-spacing:1px}
.top-mail{left:498px;top:14px;font-size:10px;color:var(--white);display:flex;align-items:center;gap:5px}
.follow{display:flex;align-items:center;gap:3px;font-size:11px;color:var(--white)}
.top-follow{left:624px;top:12px}
.social{width:16px;height:16px;display:inline-block;border-radius:2px}
.s-friend{background:#3b5a9a}.s-chirp{background:#2aa8e0}.s-link{background:#0e76a8}
.call{left:501px;top:36px;font-size:18px;color:var(--white)}
.call b{color:var(--orange);font-weight:700}

/* nav */
.nav{left:0;top:73px;width:833px;height:32px;background:linear-gradient(#35b5ec,var(--sky-dark))}
.nav ul{list-style:none;display:flex;position:absolute;left:117px;top:0;height:32px}
.nav li{font-size:12px;color:var(--white);height:32px;display:flex;align-items:center;padding:0 19px;border-right:1px solid rgba(255,255,255,.28)}
.nav li:last-child{border-right:none}
.nav li.active{padding:0 6px 0 7px;border-right:none}
.nav li.active span{background:#000;border-radius:4px;padding:4px 8px}

/* hero */
.hero{left:0;top:105px;width:833px;height:244px;background:linear-gradient(180deg,#55703e 0%,#8fa0a6 30%,#6c6a66 60%,#3f3a34 100%)}
.hero-arrow{top:180px;color:var(--white);font-size:22px;opacity:.8}
.caption{left:0;top:307px;width:833px;height:42px;background:rgba(0,0,0,.35)}
.caption p{position:absolute;left:109px;top:10px;font-family:"Marcellus",serif;font-size:15px;color:var(--white);letter-spacing:.5px}
.dots{left:648px;top:321px;display:flex;gap:4px}
.dots i{width:8px;height:8px;border-radius:50%;background:#999}
.dots i:first-child{background:var(--white)}

/* services */
.services{left:0;top:349px;width:833px;height:203px;background:linear-gradient(var(--navy),var(--navy-2))}
.svc{top:369px;width:220px;text-align:center;color:var(--white)}
.svc .icon{width:58px;height:58px;border-radius:50%;background:var(--white);margin:0 auto;display:flex;align-items:center;justify-content:center}
.svc h3{font-family:"PT Serif",serif;font-weight:400;font-size:13.5px;letter-spacing:.3px;margin-top:18px}
.svc p{font-size:11px;line-height:16px;margin-top:4px}
.btn-more{display:inline-block;margin-top:8px;font-family:"PT Serif",serif;font-style:italic;font-size:11px;color:#333;background:linear-gradient(#fff,#bdbdbd);border:1px solid #999;padding:1px 7px}
.divider{top:444px;width:1px;height:60px;background:rgba(255,255,255,.2)}

/* about */
.about-title{left:108px;top:570px;font-size:21px;color:var(--sky)}
.about-text{left:108px;top:602px;width:410px;font-size:7.6px;line-height:14.5px;text-align:justify;color:#444}
.about-text p+p{margin-top:14px}

/* search */
.search{left:562px;top:565px;width:172px;height:229px;background:var(--white);border-radius:4px}
.search h4{position:absolute;left:14px;top:8px;font-weight:400;font-size:12.5px;color:var(--sky)}
.sel{position:absolute;height:14px;border:1px solid #999;background:#fff;font-size:7.5px;padding:1px 4px;color:#333}
.sel::after{content:"▾";position:absolute;right:3px;top:0;font-size:8px}
.radio{position:absolute;top:59px;font-size:8px;color:var(--sky);display:flex;align-items:center;gap:5px}
.radio i{width:12px;height:12px;border-radius:50%;border:1px solid #888;background:radial-gradient(#666 30%,#ddd 35%)}
.radio.off i{background:#ddd}
.list{position:absolute;left:18px;top:160px;width:135px;height:50px;border:1px solid #999;font-size:7.5px;line-height:10px;color:#222;overflow:hidden}
.list div{padding-left:2px}
.list .hl{background:#cfcfcf}
.btn-search{position:absolute;left:97px;top:218px;width:60px;height:22px;background:var(--sky);border-radius:4px;color:var(--white);font-size:9px;display:flex;align-items:center;justify-content:center}

/* projects */
.proj-line{left:102px;top:829px;width:637px;height:1px;background:#c9d6e4}
.proj-tab{left:326px;top:829px;width:195px;height:22px;background:linear-gradient(#1d6bb4,#0b4787);clip-path:polygon(0 0,100% 0,94% 100%,6% 100%);color:var(--white);font-size:14px;font-weight:700;text-align:center;line-height:22px}
.proj-band{left:102px;top:870px;width:637px;height:126px;background:linear-gradient(#fff,#e4e4e4);box-shadow:0 3px 4px rgba(0,0,0,.25)}
.arrow-btn{top:922px;width:17px;height:17px;border-radius:50%;background:var(--navy);color:var(--white);font-size:9px;display:flex;align-items:center;justify-content:center}
.card{top:882px;width:131px;height:98px;border:1px solid #aaa;overflow:hidden}
.card .photo{width:100%;height:100%}
.card .label{position:absolute;left:0;bottom:0;width:100%;height:25px;background:rgba(21,110,190,.85);padding:2px 7px;color:var(--white);font-size:8px;line-height:10px}
.card .label em{display:block}

/* footer */
.footer{left:0;top:1029px;width:833px;height:171px;background:var(--footer);border-top:3px solid var(--orange)}
.f-h{top:1047px;font-size:11.5px;font-weight:700;color:var(--white);padding-bottom:6px;border-bottom:1px solid #555}
.f-links{top:1074px;font-size:9px;color:var(--footer-text);list-style:none;line-height:18.3px}
.f-links li::before{content:"›";margin-right:5px}
.f-text{font-size:9px;color:var(--footer-text);line-height:15px}
.f-input{left:278px;top:1110px;width:138px;height:17px;background:#fff;border-radius:2px;font-size:8.5px;font-style:italic;color:#888;padding:2px 5px}
.f-btn{left:278px;top:1137px;width:79px;height:19px;background:linear-gradient(#ffa638,#e0700a);border-radius:3px;font-size:10px;font-weight:700;color:#111;text-align:center;line-height:19px}
.f-row{left:456px;font-size:9px;color:var(--footer-text);display:flex;gap:10px;align-items:flex-start}
.f-row svg{flex:none;margin-top:1px}
.f-brand{left:608px;top:1075px;font-size:36px;color:var(--white)}
.f-follow{left:617px;top:1143px;font-weight:700}
.copy{left:0;top:1175px;width:833px;border-top:1px solid #444;font-size:9px;color:var(--white);text-align:center;padding-top:6px}
</style>
</head>
<body>

<header>
  <div class="abs topbar"></div>
  <div class="abs brand">Dwell-On</div>
  <div class="abs top-mail">
    <svg width="11" height="8" viewBox="0 0 11 8"><rect x=".5" y=".5" width="10" height="7" fill="none" stroke="#fff"/><path d="M.5 .5 5.5 4.5 10.5 .5" fill="none" stroke="#fff"/></svg>
    info@dwellon.co.uk
  </div>
  <div class="abs follow top-follow">Follow Us:
    <span class="social s-friend" aria-label="Friendlane"></span>
    <span class="social s-chirp" aria-label="chirpnet"></span>
    <span class="social s-link" aria-label="Linkwork"></span>
  </div>
  <div class="abs call">CALL US TODAY: <b>020 7946 0321</b></div>
</header>

<nav class="abs nav">
  <ul>
    <li class="active"><span>Home</span></li>
    <li>Buy</li><li>Sell</li><li>Rent</li><li>Auction</li><li>Home Opens</li><li>About Us</li><li>Services</li><li>Contact Us</li>
  </ul>
</nav>

<section>
  <div class="abs hero" role="img" aria-label="Photo of a two-storey brick house at dusk with lit windows, garage and trees"></div>
  <div class="abs hero-arrow" style="left:118px">‹</div>
  <div class="abs hero-arrow" style="left:698px">›</div>
  <div class="abs caption"><p>SUPERBLY LOCATED, INVITINGLY READY TO ENJOY</p></div>
  <div class="abs dots"><i></i><i></i><i></i><i></i><i></i></div>
</section>

<section>
  <div class="abs services"></div>
  <div class="abs divider" style="left:302px"></div>
  <div class="abs divider" style="left:534px"></div>
  <div class="abs svc" style="left:76px">
    <div class="icon"><svg width="26" height="26" viewBox="0 0 26 26"><path d="M4 22 20 6M6 4l16 16" stroke="#111" stroke-width="3" stroke-linecap="round"/></svg></div>
    <h3>PROPERTY MANAGEMENT</h3>
    <p>Lorem ipsum dolor sit amet,<br>consectetuer adipiscing consequat.</p>
    <span class="btn-more">Read More</span>
  </div>
  <div class="abs svc" style="left:308px">
    <div class="icon"><svg width="26" height="26" viewBox="0 0 26 26"><path d="M3 12l6-5 5 3 5-3 5 5-9 8z" fill="#111"/></svg></div>
    <h3>PROPERTY CONSULTING</h3>
    <p>Lorem ipsum dolor sit amet,<br>consectetuer adipiscing consequat.</p>
    <span class="btn-more">Read More</span>
  </div>
  <div class="abs svc" style="left:541px">
    <div class="icon"><svg width="26" height="26" viewBox="0 0 26 26"><path d="M6 12 13 5l7 7v6H6z" fill="none" stroke="#111" stroke-width="2.2"/><path d="M3 21h20" stroke="#111" stroke-width="2.2"/></svg></div>
    <h3>OTHER SERVICES</h3>
    <p>Lorem ipsum dolor sit amet,<br>consectetuer adipiscing consequat.</p>
    <span class="btn-more">Read More</span>
  </div>
</section>

<section>
  <h2 class="abs about-title" style="font-weight:400">About Dwell-On</h2>
  <div class="abs about-text">
    <p>Lorem ipsum dolor sit amet, consectetur adipiscing elit. Sed vitae nisi metus. Quisque quis nibh at risus mollis commodo. Vivamus hendrerit sit amet nulla ac commodo. Curabitur a laoreet augue. Aenean sed vestibulum arcu, eu posuere ex. Nam scelerisque porta risus, eu iaculis urna porta quis. In cursus diam vitae eros feugiat ultricies. Maecenas id nulla magna. Vivamus varius ligula tellus, id placerat eros egestas ut. Sed imperdiet elit vel mollis cursus. Curabitur aliquam posuere purus in fermentum. Nulla suscipit nunc tempor lacinia molestie. Ut eget leo sed lorem iaculis ullamcorper. Suspendisse fringilla, nibh vitae volutpat facilisis, metus nisi finibus libero, nec rutrum est risus sed massa.</p>
    <p>Nulla lacinia lacus aliquam nibh ullamcorper gravida. Vivamus a nunc venenatis, imperdiet magna vitae, eleifend nisi. Nulla odio elit, sodales laoreet risus ut, efficitur euismod neque. Vestibulum egestas aliquam velit, vel hendrerit magna fermentum vitae. Sed molestie orci et urna imperdiet accumsan. Vivamus eget ex in diam tristique malesuada quis id est. Donec nec mauris eget enim malesuada fermentum. Sed ultricies urna eget nisl suscipit, eget ornare diam euismod. Nulla accumsan orci eu risus tristique imperdiet. Duis interdum, mi non convallis fringilla, arcu turpis interdum nisi, et sagittis risus mi id tortor. Pellentesque bibendum pharetra arcu sed vestibulum.</p>
  </div>

  <form class="abs search">
    <h4>Quick Search</h4>
    <div class="sel" style="left:18px;top:33px;width:135px">Residential Search</div>
    <div class="radio" style="left:24px"><i></i>BUY</div>
    <div class="radio off" style="left:64px"><i></i>RENT</div>
    <div class="sel" style="left:18px;top:88px;width:63px">Price Min</div>
    <div class="sel" style="left:90px;top:88px;width:63px">Price Max</div>
    <div class="sel" style="left:18px;top:114px;width:63px">Bedrooms</div>
    <div class="sel" style="left:90px;top:114px;width:63px">Bathrooms</div>
    <div class="sel" style="left:18px;top:140px;width:135px">All Types</div>
    <div class="list"><div class="hl">All Suburbs</div><div>Abbey</div><div>Alfred Cove</div><div>Armadale</div><div>Attadale</div></div>
    <div class="btn-search">Search</div>
  </form>
</section>

<section>
  <div class="abs proj-line"></div>
  <h2 class="abs proj-tab">Our Projects</h2>
  <div class="abs proj-band"></div>
  <div class="abs arrow-btn" style="left:110px">◂</div>
  <div class="abs arrow-btn" style="left:711px">▸</div>
  <div class="abs card" style="left:136px"><div class="photo" role="img" aria-label="Modern glass office building under blue sky" style="background:linear-gradient(#4f86c6,#b9c6d3 60%,#6c7c8c)"></div><div class="label"><em>Project Name</em>Duis autem vel eum</div></div>
  <div class="abs card" style="left:281px"><div class="photo" role="img" aria-label="Row of brick townhouses" style="background:linear-gradient(#8fb2d4,#9a5b43 45%,#6b4a3a)"></div><div class="label"><em>Project Name</em>Duis autem vel eum</div></div>
  <div class="abs card" style="left:425px"><div class="photo" role="img" aria-label="Luxury villa entrance with palm trees" style="background:linear-gradient(#6f8fb0,#c9b49a 45%,#7a6a5a)"></div><div class="label"><em>Project Name</em>Duis autem vel eum</div></div>
  <div class="abs card" style="left:569px"><div class="photo" role="img" aria-label="City office towers" style="background:linear-gradient(#a8c4e0,#c8c8c2 50%,#8d8a82)"></div><div class="label"><em>Project Name</em>Duis autem vel eum</div></div>
</section>

<footer>
  <div class="abs footer"></div>
  <h4 class="abs f-h" style="left:102px;width:140px">QUICK LINKS</h4>
  <ul class="abs f-links" style="left:100px"><li>Home</li><li>About Us</li><li>Our Services</li><li>Rental Property</li><li>Property for Sale</li></ul>
  <ul class="abs f-links" style="left:184px"><li>Contact Us</li><li>FAQ's</li></ul>

  <h4 class="abs f-h" style="left:279px;width:138px">NEWLETTERS &amp; UPDATES</h4>
  <p class="abs f-text" style="left:279px;top:1075px">Get latest updates by entering<br>your email address</p>
  <div class="abs f-input">Email Address</div>
  <div class="abs f-btn">SUBSCRIBE</div>

  <h4 class="abs f-h" style="left:456px;width:118px">CONTACT INFO</h4>
  <div class="abs f-row" style="top:1075px"><svg width="9" height="12" viewBox="0 0 9 12"><path d="M4.5 12C1 7 0 6 0 4.5a4.5 4.5 0 0 1 9 0C9 6 8 7 4.5 12z" fill="#aaa"/><circle cx="4.5" cy="4.5" r="1.6" fill="#2a2a2a"/></svg><span style="line-height:12px">Street Name, City Name<br>Zip Code - 00000</span></div>
  <div class="abs f-row" style="top:1105px"><svg width="10" height="10" viewBox="0 0 10 10"><path d="M2 0 4 3 3 4.5Q4.5 6.5 5.5 7L7 6l3 2-1 2Q4 10 0 2z" fill="#aaa"/></svg>123-456-7890</div>
  <div class="abs f-row" style="top:1125px"><svg width="11" height="10" viewBox="0 0 11 10"><rect x="2" y="0" width="7" height="3" fill="#aaa"/><rect x="0" y="3" width="11" height="5" rx="1" fill="#aaa"/><rect x="2" y="6" width="7" height="4" fill="#ccc"/></svg>123-456-7890</div>
  <div class="abs f-row" style="top:1147px"><svg width="10" height="8" viewBox="0 0 10 8"><rect width="10" height="8" fill="#aaa"/><path d="M0 0 5 4 10 0" fill="none" stroke="#2a2a2a"/></svg>info@dwellon.co.uk</div>

  <div class="abs f-brand">Dwell-On</div>
  <div class="abs follow f-follow">Follow Us
    <span class="social s-friend" aria-label="Friendlane"></span>
    <span class="social s-chirp" aria-label="chirpnet"></span>
    <span class="social s-link" aria-label="Linkwork"></span>
  </div>
  <p class="abs copy">Copyright © 2014 – www.dwellon-homes.co.uk – All rights reserved</p>
</footer>

</body>
</html>
```